Dewleaf Botanica. Home based organic skin care manufacturer

We need top notch user friendly and interactive web6/mobile site that will cater to online e commerce, retail of our varieties of products and real time communication with online buyers.

```html
<!DOCTYPE html>
<html lang="en">
<head>
<meta charset="utf-8">
<title>Dewleaf Botanica</title>
<link href="https://fonts.googleapis.com/css2?family=Abhaya+Libre:wght@400;700;800&family=Roboto:wght@400;500&family=Open+Sans:wght@700&display=swap" rel="stylesheet">
<style>
:root{
  --green:#7cb50b;
  --green-band:#93bf2e;
  --olive-bar:#718f3a;
  --ink:#111;
  --muted:#333;
  --white:#fff;
  --line:#e6e6e6;
  --grey-btn:#e4e4e4;
  --footer:#000;
}
*{box-sizing:border-box;margin:0;padding:0}
html,body{width:1200px;height:2826px;overflow:hidden;background:var(--white)}
body{position:relative;font-family:'Abhaya Libre',serif;color:var(--ink)}
.abs{position:absolute}

/* hero */
.hero{left:0;top:0;width:1200px;height:574px;overflow:hidden;
  background:linear-gradient(100deg,#4f8d98 0%,#6fa2a8 35%,#9fb7b2 55%,#c9b8a7 75%,#b49a86 100%)}
.hero-photo{position:absolute;inset:0;background:radial-gradient(ellipse at 78% 55%,rgba(232,210,190,.8) 0%,rgba(200,180,160,.3) 35%,transparent 60%),radial-gradient(ellipse at 15% 80%,rgba(160,60,50,.45),transparent 40%)}
.hero-line{position:absolute;inset:0}
.brand{font-family:'Abhaya Libre',serif;font-weight:700;color:var(--white);display:flex;align-items:center;gap:10px}
.brand-dot{width:14px;height:14px;border-radius:50%;background:var(--white)}
.hero .brand{left:99px;top:52px;font-size:28px}
.nav{top:24px;left:450px;display:flex;gap:0;font-weight:800;font-size:19px;color:var(--white)}
.nav a{color:inherit;text-decoration:none;position:absolute;white-space:nowrap}
.nav .active{border-left:3px solid var(--white);padding-left:8px}
.nav-icon{top:26px}
.hero-title{left:99px;top:170px;color:var(--white);font-weight:800;line-height:1}
.hero-title .l1{font-size:64px;display:block}
.hero-title .l2{font-size:92px;display:block;margin-top:12px}
.hero-sub{left:107px;top:358px;color:var(--white);font-weight:800;font-size:19px;line-height:27px;width:300px}

/* sections */
.section-title{font-weight:800;font-size:35px;line-height:1.1;color:var(--ink)}
.lead{font-size:18px;line-height:25px;color:var(--muted)}
.arrow{width:42px;height:42px;border-radius:50%;display:flex;align-items:center;justify-content:center}
.arrow.on{background:var(--green)}
.arrow.off{background:var(--grey-btn)}
.card{background:var(--white);border:1px solid var(--line);border-radius:6px}
.card.raised{box-shadow:0 4px 14px rgba(0,0,0,.14);border-color:#eee}
.product-shot{position:absolute;border-radius:4px}
.card-name{position:absolute;left:0;right:0;text-align:center;font-weight:800;font-size:20px;line-height:25px}
.btn-cart{position:absolute;background:var(--green);color:var(--white);font-weight:800;font-size:17px;border-radius:4px;display:flex;align-items:center;justify-content:center}

.tile{position:absolute;top:1186px;height:430px;width:285px;display:flex;align-items:flex-end;justify-content:center;padding-bottom:44px}
.tile span{color:var(--white);font-weight:800;font-size:29px;line-height:37px;text-align:center}

/* band */
.band{left:0;top:2057px;width:1200px;height:356px;background:linear-gradient(90deg,#8fbc2a 0%,#9cc63a 50%,#8bb826 100%)}
.band-title{left:0;width:1200px;top:2132px;text-align:center;color:var(--white);font-weight:800;font-size:40px}
.btn-outline{top:2205px;height:45px;width:148px;border:2px solid var(--white);border-radius:4px;color:var(--white);font-weight:800;font-size:22px;display:flex;align-items:center;justify-content:center}
.features{left:86px;top:2361px;width:1029px;height:67px;background:var(--olive-bar);display:flex;align-items:center;justify-content:center;gap:18px;font-family:'Open Sans',sans-serif;font-size:11.5px;color:var(--white);letter-spacing:.3px;z-index:2}
.feature{display:flex;align-items:center;gap:10px}
.sep{width:44px;height:1px;background:var(--white)}

/* footer */
.footer{left:0;top:2413px;width:1200px;height:413px;background:var(--footer);color:var(--white);font-family:'Roboto',sans-serif}
.footer .brand{position:absolute;left:84px;top:150px;font-size:32px}
.social{position:absolute;top:2664px;width:33px;height:33px;border:1.5px solid var(--white);border-radius:50%}
.f-head{position:absolute;top:2480px;font-family:'Abhaya Libre',serif;font-size:24px;color:var(--white)}
.f-head::after{content:"";position:absolute;left:0;top:38px;width:32px;height:2px;background:var(--white)}
.f-text{position:absolute;font-family:'Roboto',sans-serif;font-size:14.5px;color:var(--white);line-height:23px}
.rule{left:111px;top:2743px;width:977px;height:1px;background:#aaa}
.copy{left:0;width:1200px;top:2780px;text-align:center;font-family:'Roboto',sans-serif;font-size:16px;color:var(--white)}
.email-box{left:810px;top:2605px;width:276px;height:40px;background:var(--white);border-radius:20px;display:flex;align-items:center;justify-content:space-between;padding:0 14px 0 20px;font-family:'Roboto',sans-serif;font-size:12.5px;color:#222}
</style>
</head>
<body>

<!-- Hero -->
<header class="abs hero">
  <div class="hero-photo" role="img" aria-label="Woman relaxing with a cream face mask among tropical flowers"></div>
  <svg class="hero-line" width="1200" height="574" viewBox="0 0 1200 574">
    <line x1="-4" y1="574" x2="1204" y2="-4" stroke="#fff" stroke-width="5"/>
  </svg>
  <div class="abs brand"><span class="brand-dot"></span>Dewleaf Botanica</div>
  <nav class="abs nav">
    <a class="active" style="left:0">Home</a>
    <a style="left:102px">Skin Care</a>
    <a style="left:224px">Home based organic</a>
    <a style="left:428px">About Us</a>
  </nav>
  <svg class="abs nav-icon" style="left:984px" width="20" height="20" viewBox="0 0 20 20"><circle cx="8" cy="8" r="6" fill="none" stroke="#fff" stroke-width="2.6"/><line x1="12.5" y1="12.5" x2="18" y2="18" stroke="#fff" stroke-width="3"/></svg>
  <svg class="abs nav-icon" style="left:1034px" width="18" height="20" viewBox="0 0 18 20"><circle cx="9" cy="5" r="5" fill="#fff"/><path d="M0 20c0-6 4-9 9-9s9 3 9 9z" fill="#fff"/></svg>
  <svg class="abs nav-icon" style="left:1078px" width="22" height="20" viewBox="0 0 22 20"><path d="M0 2h4l3 11h11l3-8H6" fill="none" stroke="#fff" stroke-width="2.4"/><path d="M6 5h15l-3 8H8z" fill="#fff"/><circle cx="9" cy="17" r="2" fill="#fff"/><circle cx="17" cy="17" r="2" fill="#fff"/></svg>
  <h1 class="abs hero-title"><span class="l1">DEWLEAF</span><span class="l2">BOTANICA</span></h1>
  <p class="abs hero-sub">HOME BASED ORGANIC SKIN CARE MANUFACTURER.</p>
</header>

<!-- Our skin care -->
<h2 class="abs section-title" style="left:92px;top:700px">OUR SKIN CARE</h2>
<p class="abs lead" style="left:92px;top:761px;width:262px">Lorem ipsum dolor sit amet, consectetur adipiscing elit, sed do eiusmod tempor incididunt ut labore et dolore magna aliqua. Ut enim ad minim veniam, quis nostrud exercitation ullamco laboris nisi ut</p>
<div class="abs arrow on" style="left:91px;top:931px"><svg width="14" height="14" viewBox="0 0 14 14"><path d="M9 2L4 7l5 5" fill="none" stroke="#fff" stroke-width="2.2"/></svg></div>
<div class="abs arrow off" style="left:144px;top:931px"><svg width="14" height="14" viewBox="0 0 14 14"><path d="M5 2l5 5-5 5" fill="none" stroke="#666" stroke-width="2"/></svg></div>

<div class="abs card" style="left:370px;top:681px;width:227px;height:280px">
  <div class="product-shot" style="left:84px;top:18px;width:58px;height:172px;background:linear-gradient(180deg,#f0f0f0 0 24%,#f2cf44 24% 100%)" role="img" aria-label="Glow oil bottle"></div>
  <div class="card-name" style="top:204px">Glow Oil</div>
</div>
<div class="abs card raised" style="left:613px;top:681px;width:227px;height:302px">
  <div class="product-shot" style="left:84px;top:18px;width:58px;height:176px;background:linear-gradient(180deg,#ececec 0 22%,#fafafa 22% 100%);box-shadow:inset 0 0 0 1px #e2e2e2" role="img" aria-label="Face cleansing wash bottle"></div>
  <div class="card-name" style="top:204px">Face Cleansing Wash</div>
  <div class="btn-cart" style="left:44px;top:245px;width:139px;height:39px">ADD TO CART</div>
</div>
<div class="abs card" style="left:857px;top:681px;width:227px;height:280px">
  <div class="product-shot" style="left:34px;top:48px;width:150px;height:120px;background:linear-gradient(180deg,#c9c9c9 0 12%,#f6f6f4 12% 100%)" role="img" aria-label="Brightening body milk jar"></div>
  <div class="card-name" style="top:204px">Brightening Body<br>Milk</div>
</div>

<!-- Varieties -->
<h2 class="abs section-title" style="left:0;width:1200px;text-align:center;top:1104px">OUR VARIETIES OF PRODUCTS</h2>
<div class="tile" style="left:10px;background:linear-gradient(180deg,#e6d2e4 0%,#b47eb6 50%,#80398b 100%)" role="img" aria-label="Facial treatment with mask brush"><span>FACIALS</span></div>
<div class="tile" style="left:304px;background:linear-gradient(180deg,#c9d0d6 0%,#9a9ea3 55%,#4a4d52 100%)" role="img" aria-label="Bearded man in profile"><span>HAIR AND BEARD<br>CARE</span></div>
<div class="tile" style="left:599px;background:linear-gradient(180deg,#e7d7c3 0%,#c69a78 55%,#6e4a3a 100%)" role="img" aria-label="Smiling woman touching her cheek"><span>TREATMENTS</span></div>
<div class="tile" style="left:893px;background:linear-gradient(180deg,#dbe3ee 0%,#8fa6c3 55%,#2d4d7f 100%)" role="img" aria-label="Child in winter hat applying cream"><span>KIDDIES GLOW KIT</span></div>

<!-- New products -->
<div class="abs card raised" style="left:92px;top:1672px;width:227px;height:303px">
  <div class="product-shot" style="left:34px;top:30px;width:148px;height:150px;background:linear-gradient(180deg,#a9a23a 0 30%,#f4f2ee 30% 100%)" role="img" aria-label="Balancing facial toner jar"></div>
  <div class="card-name" style="top:204px">Balancing Facial Toner</div>
  <div class="btn-cart" style="left:45px;top:246px;width:139px;height:38px">ADD TO CART</div>
</div>
<div class="abs card" style="left:336px;top:1672px;width:227px;height:277px">
  <div class="product-shot" style="left:32px;top:32px;width:158px;height:148px;background:linear-gradient(180deg,#a9a23a 0 30%,#f4f2ee 30% 100%)" role="img" aria-label="Age reverse serum jar"></div>
  <div class="card-name" style="top:204px">Age Reverse Serum</div>
</div>
<div class="abs card" style="left:579px;top:1672px;width:227px;height:277px">
  <div class="product-shot" style="left:34px;top:28px;width:154px;height:150px;background:linear-gradient(180deg,#f7f7f3 0 32%,#f0e9d8 32% 100%)" role="img" aria-label="Face and body scrub jar"></div>
  <div class="card-name" style="top:204px">Face and body scrub</div>
</div>
<h2 class="abs section-title" style="left:828px;width:256px;text-align:right;top:1686px">OUR NEW<br>PRODUCTS</h2>
<p class="abs lead" style="left:824px;width:260px;text-align:right;top:1777px">Lorem ipsum dolor sit amet, consectetur adipiscing elit, sed do eiusmod tempor incididunt ut labore et dolore magna aliqua.</p>
<div class="abs arrow off" style="left:990px;top:1897px"><svg width="14" height="14" viewBox="0 0 14 14"><path d="M9 2L4 7l5 5" fill="none" stroke="#333" stroke-width="2"/></svg></div>
<div class="abs arrow on" style="left:1042px;top:1897px"><svg width="14" height="14" viewBox="0 0 14 14"><path d="M5 2l5 5-5 5" fill="none" stroke="#fff" stroke-width="2.2"/></svg></div>

<!-- Communication band -->
<section class="abs band" role="img" aria-label="Green tinted backdrop of oil bottles and leaves"></section>
<h2 class="abs band-title">Real-Time Communication With Online Buyers.</h2>
<div class="abs btn-outline" style="left:442px">Retail</div>
<div class="abs btn-outline" style="left:610px">Buyers.</div>
<div class="abs features">
  <div class="feature"><svg width="32" height="20" viewBox="0 0 32 20"><rect x="1" y="3" width="19" height="12" fill="none" stroke="#fff" stroke-width="1.5"/><path d="M20 7h6l4 4v4h-10" fill="none" stroke="#fff" stroke-width="1.5"/><circle cx="7" cy="17" r="2.2" fill="#718f3a" stroke="#fff" stroke-width="1.5"/><circle cx="25" cy="17" r="2.2" fill="#718f3a" stroke="#fff" stroke-width="1.5"/></svg>FAST &amp; PROMPT DELIVERY</div>
  <div class="sep"></div>
  <div class="feature"><svg width="16" height="22" viewBox="0 0 16 22"><rect x="1" y="9" width="14" height="12" fill="none" stroke="#fff" stroke-width="1.5"/><path d="M4 9V5a4 4 0 018 0v4" fill="none" stroke="#fff" stroke-width="1.5"/></svg>SECURE PAYMENT</div>
  <div class="sep"></div>
  <div class="feature"><svg width="18" height="18" viewBox="0 0 18 18"><rect x="1" y="1" width="16" height="16" rx="2" fill="none" stroke="#fff" stroke-width="1.5"/><path d="M5 9l3 3 5-6" fill="none" stroke="#fff" stroke-width="1.5"/></svg>100% GUARANTEED</div>
  <div class="sep"></div>
  <div class="feature"><svg width="26" height="22" viewBox="0 0 26 22"><rect x="1" y="5" width="24" height="16" rx="2" fill="none" stroke="#fff" stroke-width="1.5"/><path d="M4 5l12-4 2 4" fill="none" stroke="#fff" stroke-width="1.5"/><rect x="17" y="10" width="8" height="6" fill="none" stroke="#fff" stroke-width="1.5"/></svg>MONEY BACK GUARANTEED</div>
</div>

<!-- Footer -->
<footer class="abs footer">
  <div class="brand"><span class="brand-dot"></span>Dewleaf Botanica</div>
</footer>
<span class="social" style="left:100px" aria-label="Video channel"></span>
<span class="social" style="left:138px" aria-label="Photo channel"></span>

<h3 class="f-head" style="left:363px">More Info</h3>
<p class="f-text" style="left:363px;top:2537px;line-height:30px">Terms &amp; Conditions<br>Privacy Policy<br>About Us<br>Support</p>

<h3 class="f-head" style="left:561px">Contact Us</h3>
<p class="f-text" style="left:561px;top:2535px;width:180px">ADDRESS</p>
<p class="f-text" style="left:561px;top:2558px;width:180px"><svg width="9" height="13" viewBox="0 0 9 13"><path d="M4.5 0A4.5 4.5 0 000 4.5C0 8 4.5 13 4.5 13S9 8 9 4.5A4.5 4.5 0 004.5 0z" fill="#fff"/><circle cx="4.5" cy="4.5" r="1.6" fill="#000"/></svg> Lorem ipsum dolor sit amet, consectetur</p>
<p class="f-text" style="left:561px;top:2614px">PHONE</p>
<p class="f-text" style="left:561px;top:2637px"><svg width="12" height="12" viewBox="0 0 12 12"><path d="M2 0l3 3-1.5 1.8a7 7 0 003.7 3.7L9 7l3 3-1.8 2C5 12 0 7 0 1.8z" fill="#fff"/></svg> +1 555-014-2290</p>
<p class="f-text" style="left:561px;top:2673px">EMAIL</p>
<p class="f-text" style="left:561px;top:2696px;font-size:16px"><svg width="14" height="11" viewBox="0 0 14 11"><rect width="14" height="11" rx="1" fill="#fff"/><path d="M0 1l7 5 7-5" fill="none" stroke="#000" stroke-width="1.3"/></svg> hello@dewleafbotanica.com</p>

<h3 class="f-head" style="left:813px">Newsletter</h3>
<p class="f-text" style="left:813px;top:2535px;width:280px">Lorem ipsum dolor sit amet, consectetur adipiscing elit, sed do eiusmod tempor</p>
<div class="abs email-box">Enter Email<svg width="18" height="18" viewBox="0 0 18 18"><circle cx="9" cy="9" r="9" fill="#000"/><path d="M4 9l9-4-3 9-2-3z" fill="#fff"/></svg></div>

<div class="abs rule"></div>
<p class="abs copy">© copyrights 2023 Dewleaf Botanica | &nbsp;All Rights Reserved</p>

</body>
</html>
```